Business Card Design

Just looking for a good designs that looks good with our company logo. I'd like it to be simple and to the point. Just including contact information, our logo, and my name somewhere on the card so future clients know who they're contacting, and a couple services offered. The two images I attached are pictures of our logo. I don't care which color they they are, I just attached both images to give a reference of logo colors depending on the color of the card.
Names: Calvin Prewitt
Phone: 555-247-9061
Email: tidyturfcrew@mailvista.net
Services offered:
Mowing
Fertilization
Aeration
Bed & tree maintenance
and more.
Industry/Entity Type
Business
Contact Information for Business Card
Names: Calvin Prewitt
Phone: 555-247-9061
Look and feel

```html
<!DOCTYPE html>
<html lang="en">
<head>
<meta charset="utf-8">
<title>Tidy Turf Crew – Business Card</title>
<link rel="stylesheet" href="https://fonts.googleapis.com/css2?family=Open+Sans:wght@400;600;700&family=Oswald:wght@600&display=swap">
<style>
  :root {
    --page-bg: #e4e4e4;
    --card-dark: #1f1f1f;
    --grass-light: #5fae32;
    --grass-mid: #3f8f22;
    --grass-deep: #2a6a16;
    --accent-red: #d8392b;
    --accent-yellow: #f2d82a;
    --accent-orange: #c5562a;
    --text-light: #e8e8e8;
    --text-dark: #14200c;
  }
  html, body {
    margin: 0;
    width: 1200px;
    height: 1200px;
    overflow: hidden;
    background: var(--page-bg);
    font-family: "Open Sans", Arial, sans-serif;
  }
  .stage {
    width: 1200px;
    height: 1200px;
    display: flex;
    align-items: center;
    justify-content: center;
  }
  .business-card {
    position: relative;
    width: 1050px;
    height: 600px;
    background: var(--card-dark);
    overflow: hidden;
    box-shadow: 0 10px 30px rgba(0,0,0,0.18);
  }
  .grass-field {
    position: absolute;
    left: 0;
    right: 0;
    top: 300px;
    bottom: 0;
    background: linear-gradient(180deg, var(--grass-mid) 0%, var(--grass-light) 45%, var(--grass-mid) 80%, var(--grass-deep) 100%);
  }
  .brand {
    position: absolute;
    left: 90px;
    top: 175px;
    display: flex;
    align-items: center;
    gap: 22px;
  }
  .brand-dot {
    width: 74px;
    height: 74px;
    border-radius: 50%;
    background: var(--accent-yellow);
  }
  .brand-name {
    font-family: "Oswald", "Open Sans", sans-serif;
    font-weight: 600;
    font-size: 64px;
    letter-spacing: 1px;
    color: var(--accent-yellow);
    line-height: 1;
  }
  .services {
    position: absolute;
    left: 640px;
    top: 110px;
    color: var(--text-light);
    font-size: 27px;
    line-height: 1.25;
  }
  .services-title {
    font-size: 22px;
    margin: 0 0 4px 38px;
  }
  .services-list {
    list-style: none;
    margin: 0;
    padding: 0;
  }
  .services-list li {
    display: flex;
    align-items: center;
    gap: 12px;
  }
  .services-list .more {
    padding-left: 0;
  }
  .tick {
    width: 24px;
    height: 18px;
    flex: none;
  }
  .holder-name {
    position: absolute;
    left: 240px;
    top: 388px;
    font-weight: 700;
    font-size: 32px;
    color: var(--text-dark);
  }
  .contact {
    position: absolute;
    left: 560px;
    top: 430px;
    color: var(--text-dark);
    font-size: 28px;
    line-height: 1.5;
  }
  .contact-row {
    display: flex;
    align-items: center;
    gap: 14px;
  }
  .contact-icon {
    width: 24px;
    height: 24px;
    flex: none;
  }
</style>
</head>
<body>
<main class="stage">
  <article class="business-card">
    <div class="grass-field" role="img" aria-label="Photograph of a freshly mown green lawn"></div>

    <div class="brand">
      <span class="brand-dot"></span>
      <span class="brand-name">TIDY TURF CREW</span>
    </div>

    <section class="services">
      <p class="services-title">Services offered:</p>
      <ul class="services-list">
        <li><svg class="tick" viewBox="0 0 24 18"><rect width="24" height="18" rx="3" fill="var(--accent-red)"/><path d="M6 9l4 4 8-8" stroke="#fff" stroke-width="2.5" fill="none"/></svg>Mowing</li>
        <li><svg class="tick" viewBox="0 0 24 18"><rect width="24" height="18" rx="3" fill="var(--accent-red)"/><path d="M6 9l4 4 8-8" stroke="#fff" stroke-width="2.5" fill="none"/></svg>Fertilization</li>
        <li><svg class="tick" viewBox="0 0 24 18"><rect width="24" height="18" rx="3" fill="var(--accent-red)"/><path d="M6 9l4 4 8-8" stroke="#fff" stroke-width="2.5" fill="none"/></svg>Aeration</li>
        <li><svg class="tick" viewBox="0 0 24 18"><rect width="24" height="18" rx="3" fill="var(--accent-red)"/><path d="M6 9l4 4 8-8" stroke="#fff" stroke-width="2.5" fill="none"/></svg>Bed &amp; tree maintenance</li>
        <li class="more">and more.</li>
      </ul>
    </section>

    <p class="holder-name">Calvin Prewitt</p>

    <div class="contact">
      <div class="contact-row">
        <svg class="contact-icon" viewBox="0 0 24 24"><rect width="24" height="24" rx="4" fill="var(--accent-red)"/><path d="M8 5h3l1 4-2 1.5a9 9 0 0 0 3.5 3.5L15 12l4 1v3a2 2 0 0 1-2 2A12 12 0 0 1 6 7a2 2 0 0 1 2-2z" fill="#fff"/></svg>
        <span>555-247-9061</span>
      </div>
      <div class="contact-row">
        <svg class="contact-icon" viewBox="0 0 24 24"><circle cx="12" cy="12" r="12" fill="var(--accent-red)"/><rect x="5" y="7.5" width="14" height="9" rx="1" fill="#fff"/><path d="M5.5 8l6.5 5 6.5-5" stroke="var(--accent-red)" stroke-width="1.5" fill="none"/></svg>
        <span>tidyturfcrew@mailvista.net</span>
      </div>
    </div>
  </article>
</main>
</body>
</html>
```